Talvo shoes is a wholesale shoe sales company , mostly working in female shoes and kiddies shoes with a small mens section . looking for a clean slick look. http://www.kemrafootwear.co.za/shop/ is a good reference

It Company

```html
<!DOCTYPE html>
<html lang="en">
<head>
<meta charset="utf-8">
<title>Talvo shoes</title>
<link rel="stylesheet" href="https://fonts.googleapis.com/css2?family=Open+Sans:wght@400;600;700&display=swap">
<style>
:root{
  --ink:#222;
  --text:#555;
  --muted:#999;
  --accent:#e0322b;
  --line:#e2e2e2;
  --band:#efefef;
  --white:#fff;
  --promo:#ececec;
  --footer:#f2f2f2;
  --shoe-light:#e9e4d2;
  --shoe-bg:#f7f6f1;
}
*{box-sizing:border-box;margin:0;padding:0}
html,body{width:1200px;height:2592px;overflow:hidden}
body{position:relative;background:var(--white);font-family:"Open Sans",Arial,sans-serif;color:var(--text)}
.abs{position:absolute}
.topbar{left:0;top:0;width:1200px;height:34px;border-bottom:1px solid var(--line)}
.welcome{left:88px;top:8px;font-size:13px;color:var(--muted)}
.welcome b{color:var(--ink)}
.cart{left:980px;top:0;height:34px;padding:0 18px;border-left:1px solid var(--line);font-size:14px;line-height:34px;color:var(--ink)}
.cart span{color:var(--accent)}
.brand{left:88px;top:80px;display:flex;align-items:center;gap:12px;font-size:50px;font-weight:600;color:var(--ink);letter-spacing:-1px}
.brand i{display:block;width:22px;height:22px;background:var(--accent)}
.search{left:968px;top:88px;width:172px;height:30px;border:1px solid var(--line);font-size:13px;color:var(--muted);padding:5px 10px}
.search svg{position:absolute;right:8px;top:7px}
.nav{left:0;top:168px;width:1200px;height:40px;border-top:1px solid var(--line);border-bottom:1px solid var(--line);display:flex;justify-content:center}
.nav a{width:212px;text-align:center;font-size:15px;font-weight:600;color:var(--ink);text-decoration:none;line-height:38px;text-transform:uppercase}
.hero{left:88px;top:232px;width:1052px;height:448px;background:linear-gradient(180deg,#ecebe9 0%,#dcdad6 55%,#a9a196 80%,#c9c4bc 100%)}
.dots{left:620px;top:656px;display:flex;gap:8px}
.dots i{width:8px;height:8px;border-radius:50%;background:#bbb}
.dots i:first-child{background:var(--accent)}
.band{left:0;top:696px;width:1200px;height:208px;background:var(--band)}
.promo{top:712px;width:312px;height:172px;background:var(--promo);border:6px solid var(--white);display:flex;align-items:center;justify-content:center;font-size:30px;color:#888}
.section-title{left:0;width:1200px;text-align:center;font-size:15px;color:var(--accent);text-transform:uppercase;letter-spacing:1px}
.card{width:312px;height:416px;border:1px solid var(--line);background:var(--white)}
.card .shot{margin:24px;height:276px;background:linear-gradient(180deg,var(--shoe-bg) 0%,var(--shoe-bg) 42%,var(--shoe-light) 42%,#ddd6c0 62%,var(--shoe-bg) 62%,var(--shoe-bg) 100%)}
.card .price{text-align:center;font-size:16px;color:var(--ink);padding-top:12px}
.card .price s{color:var(--accent);margin-right:18px}
.card .name{margin-top:14px;border-top:1px solid var(--line);text-align:center;font-size:16px;font-weight:600;color:var(--ink);padding-top:14px}
.brands{left:96px;top:1984px;width:1036px;height:164px;border:1px solid var(--line);display:flex;align-items:center;justify-content:space-around}
.brands span{font-size:30px;color:#333}
.footer{left:0;top:2192px;width:1200px;height:400px;background:var(--footer)}
.col{top:2212px;font-size:15px;color:var(--text);line-height:22px}
.col h4{font-size:15px;font-weight:700;color:var(--ink);text-transform:uppercase;margin-bottom:12px}
.col .date{font-size:12px;color:var(--muted)}
.field{width:160px;height:30px;border:1px solid #ccc;background:var(--white);font-size:13px;color:var(--muted);padding:4px 8px;display:inline-block}
.contact{display:flex;gap:10px;align-items:flex-start;margin-top:8px}
.divider{left:88px;top:2440px;width:1052px;height:1px;background:var(--line)}
.cards{left:88px;top:2458px;display:flex;gap:6px}
.cards i{width:40px;height:26px;border:1px solid #ccc;background:var(--white);border-radius:3px}
.currency{left:968px;top:2460px;display:flex;gap:14px;font-size:16px}
.currency span:first-child{color:var(--accent)}
.social{left:978px;top:2520px;display:flex;gap:14px}
.social i{width:16px;height:16px;background:#777;border-radius:50%}
.copy{left:88px;top:2552px;font-size:14px;color:var(--muted)}
</style>
</head>
<body>
<div class="abs topbar"></div>
<div class="abs welcome">Welcome Guest. <b>Sign Here</b></div>
<div class="abs cart">&#128722; Your cart <span>$125</span></div>

<div class="abs brand"><i></i>Talvo shoes</div>
<div class="abs search">Search
  <svg width="14" height="14" viewBox="0 0 14 14"><circle cx="6" cy="6" r="4.5" fill="none" stroke="#777" stroke-width="1.6"/><line x1="9.3" y1="9.3" x2="13" y2="13" stroke="#777" stroke-width="1.6"/></svg>
</div>

<nav class="abs nav"><a>Pages</a><a>Product</a><a>Features</a><a>Blog</a><a>Contact</a></nav>

<div class="abs hero" role="img" aria-label="Photograph of three casual lace-up shoes in beige, brown and navy on a light grey surface"></div>
<div class="abs dots"><i></i><i></i><i></i></div>

<div class="abs band"></div>
<div class="abs promo" style="left:96px">Promo Banner</div>
<div class="abs promo" style="left:456px">Promo Banner</div>
<div class="abs promo" style="left:820px">Promo Banner</div>

<div class="abs section-title" style="top:944px">Featured Items</div>

<div class="abs card" style="left:96px;top:1004px"><div class="shot" role="img" aria-label="Product photo of a cream canvas sneaker"></div><div class="price"><s>$120.00</s>$39.00</div><div class="name">Sample Product Talvo Shop</div></div>
<div class="abs card" style="left:456px;top:1004px"><div class="shot" role="img" aria-label="Product photo of a cream canvas sneaker"></div><div class="price"><s>$120.00</s>$39.00</div><div class="name">Sample Product Talvo Shop</div></div>
<div class="abs card" style="left:820px;top:1004px"><div class="shot" role="img" aria-label="Product photo of a cream canvas sneaker"></div><div class="price"><s>$120.00</s>$39.00</div><div class="name">Sample Product Talvo Shop</div></div>
<div class="abs card" style="left:96px;top:1440px"><div class="shot" role="img" aria-label="Product photo of a cream canvas sneaker"></div><div class="price"><s>$120.00</s>$39.00</div><div class="name">Sample Product Talvo Shop</div></div>
<div class="abs card" style="left:456px;top:1440px"><div class="shot" role="img" aria-label="Product photo of a cream canvas sneaker"></div><div class="price"><s>$120.00</s>$39.00</div><div class="name">Sample Product Talvo Shop</div></div>
<div class="abs card" style="left:820px;top:1440px"><div class="shot" role="img" aria-label="Product photo of a cream canvas sneaker"></div><div class="price"><s>$120.00</s>$39.00</div><div class="name">Sample Product Talvo Shop</div></div>

<div class="abs section-title" style="top:1930px">Designer Brands</div>
<div class="abs brands"><span>Fernwick</span><span>Baltor</span><span>Merrow</span><span>Sadie Lane</span><span>Orvale Optics</span></div>

<div class="abs footer"></div>
<div class="abs col" style="left:88px"><h4>Quick Links</h4>About Us<br>Privacy<br>Returns Policies<br>News<br>Feedback<br>Contact Us</div>
<div class="abs col" style="left:360px"><h4>Latest Post</h4>Big things are on the way<br><span class="date">posted on April 24, 2012</span><br>Product Image Galleries<br><span class="date">posted on June 12, 2012</span><br>So many options Reign in<br>feature-packed<br><span class="date">posted on May 7, 2012</span></div>
<div class="abs col" style="left:640px"><h4>Tweets</h4>Loading Tweets...</div>
<div class="abs col" style="left:912px"><h4>Newsletter</h4>
  <span class="field">Email address</span> <svg width="14" height="14" viewBox="0 0 14 14"><path d="M1 7 13 1 9 13 7 8Z" fill="#777"/></svg>
  <div class="contact"><svg width="12" height="16" viewBox="0 0 12 16"><path d="M6 0a6 6 0 0 1 6 6c0 4-6 10-6 10S0 10 0 6a6 6 0 0 1 6-6Z" fill="#777"/><circle cx="6" cy="6" r="2" fill="#f2f2f2"/></svg><span>4710 Brook Lane, Dunmore 55120<br>California</span></div>
  <div class="contact"><svg width="12" height="14" viewBox="0 0 12 14"><rect x="1" y="0" width="10" height="14" rx="2" fill="#777"/></svg><span>888-555-0192</span></div>
  <div class="contact"><svg width="14" height="12" viewBox="0 0 14 12"><rect x="0" y="1" width="14" height="10" fill="#777"/><path d="M0 1l7 5 7-5" stroke="#f2f2f2" fill="none"/></svg><span>hello@talvoshop.com</span></div>
</div>

<div class="abs divider"></div>
<div class="abs cards"><i></i><i></i><i></i><i></i></div>
<div class="abs currency"><span>USD</span><span>GBP</span><span>MYR</span><span>AUD</span></div>
<div class="abs social"><i></i><i></i><i></i><i></i><i></i><i></i></div>
<div class="abs copy">© 2012 Talvo Shop</div>
</body>
</html>
```